Tidewell Crest Housekeeping Ovu

I am looking for a car wrap design. I do not want to wrap the whole car. Id like to wrap the sides, some on the back and the hood. I am uploading a general idea of what im looking for. I’d prefer more white space than less. I’d like it to be fun without being funny or gimmicky. Back window can have some writing on it. In the examples I shared, I like the simplicity of them. It is a 2011 Ovu Palmero.

Target Market(s)

Families. We give back time to enjoy life

Industry/Entity Type

Residential cleaning

Font styles to use
Sans Serif

Colors
0054AA
0677BA
7BADD7
CADEEF
E8F1F8
E54698
E96AAD
F1A4CE
F9D9EA
FCEFF6

Requirements
Must have
• Please ck website www.tidewellcresthousekeeping.com for content and ideas. I’d like whatever is on the good to be backwards.
Should not have
• No charicaturest or cartoony stuff

```html
<!DOCTYPE html>
<html lang="en">
<head>
<meta charset="utf-8">
<title>Tidewell Crest Housekeeping – Side Wrap Layouts</title>
<link rel="stylesheet" href="https://fonts.googleapis.com/css2?family=Nunito:ital,wght@0,400;0,800;1,700&display=swap">
<style>
  :root {
    --canvas: #f3f3f3;
    --panel-white: #ffffff;
    --panel-edge: #d9d9dd;
    --brand-blue: #3953a4;
    --brand-navy: #2b3a8c;
    --brand-pink: #e2358f;
    --photo-deep: #4d56ad;
    --photo-light: #b8bce6;
  }
  * { box-sizing: border-box; margin: 0; padding: 0; }
  html, body { width: 1200px; height: 1067px; overflow: hidden; background: var(--canvas); }
  body { position: relative; font-family: "Nunito", Arial, sans-serif; }

  .wrap-panel {
    position: absolute;
    left: 40px;
    width: 1120px;
    height: 420px;
    background: var(--panel-white);
    border: 1px solid var(--panel-edge);
    border-radius: 28px;
    overflow: hidden;
  }
  .wrap-panel--driver { top: 55px; }
  .wrap-panel--passenger { top: 590px; }

  .wrap-art { position: absolute; inset: 0; width: 100%; height: 100%; }
  .wrap-art--mirrored { transform: scaleX(-1); }

  .brand-block { position: absolute; width: 470px; }
  .wrap-panel--driver .brand-block { left: 230px; top: 180px; }
  .wrap-panel--passenger .brand-block { left: 510px; top: 180px; }

  .brand-lockup { display: flex; align-items: center; gap: 12px; }
  .brand-mark { width: 44px; height: 44px; background: var(--brand-pink); border-radius: 50%; flex: none; }
  .brand-name {
    color: var(--brand-blue);
    font-size: 27px;
    font-weight: 800;
    line-height: 1.1;
    white-space: nowrap;
  }

  .tagline {
    color: var(--brand-pink);
    font-size: 17px;
    font-weight: 400;
    margin: 8px 0 0 56px;
    white-space: nowrap;
  }
  .web-address {
    color: var(--brand-navy);
    font-size: 17px;
    font-style: italic;
    font-weight: 700;
    margin: 30px 0 0 56px;
    white-space: nowrap;
  }
</style>
</head>
<body>

<section class="wrap-panel wrap-panel--driver" aria-label="Driver side wrap">
  <svg class="wrap-art" viewBox="0 0 1120 420" preserveAspectRatio="none">
    <defs>
      <linearGradient id="photoToneA" x1="0" y1="0" x2="1" y2="1">
        <stop offset="0" stop-color="var(--photo-deep)"/>
        <stop offset="1" stop-color="var(--photo-light)"/>
      </linearGradient>
    </defs>
    <path role="img" aria-label="Photo of a cleaning cloth wiping a surface" d="M640 0 H1120 V230 C980 215 860 220 770 250 C730 160 690 80 640 0Z" fill="url(#photoToneA)"/>
    <path d="M640 0 C690 80 730 160 770 250" fill="none" stroke="var(--brand-pink)" stroke-width="10"/>
    <path d="M790 225 C900 205 1000 200 1120 200 V300 C990 300 890 320 830 370 L640 370 C700 320 740 255 790 225Z" fill="var(--brand-blue)"/>
    <path d="M820 370 C880 315 990 295 1120 285 V350 C1010 350 930 360 880 370Z" fill="var(--brand-pink)"/>
  </svg>
  <div class="brand-block">
    <div class="brand-lockup">
      <span class="brand-mark"></span>
      <p class="brand-name">Tidewell Crest Housekeeping</p>
    </div>
    <p class="tagline">more time for the moments that matter</p>
    <p class="web-address">tidewellcresthousekeeping.com</p>
  </div>
</section>

<section class="wrap-panel wrap-panel--passenger" aria-label="Passenger side wrap">
  <svg class="wrap-art wrap-art--mirrored" viewBox="0 0 1120 420" preserveAspectRatio="none">
    <defs>
      <linearGradient id="photoToneB" x1="0" y1="0" x2="1" y2="1">
        <stop offset="0" stop-color="var(--photo-deep)"/>
        <stop offset="1" stop-color="var(--photo-light)"/>
      </linearGradient>
    </defs>
    <path role="img" aria-label="Photo of a cleaning cloth wiping a surface" d="M640 0 H1120 V230 C980 215 860 220 770 250 C730 160 690 80 640 0Z" fill="url(#photoToneB)"/>
    <path d="M640 0 C690 80 730 160 770 250" fill="none" stroke="var(--brand-pink)" stroke-width="10"/>
    <path d="M790 225 C900 205 1000 200 1120 200 V300 C990 300 890 320 830 370 L640 370 C700 320 740 255 790 225Z" fill="var(--brand-blue)"/>
    <path d="M820 370 C880 315 990 295 1120 285 V350 C1010 350 930 360 880 370Z" fill="var(--brand-pink)"/>
  </svg>
  <div class="brand-block">
    <div class="brand-lockup">
      <span class="brand-mark"></span>
      <p class="brand-name">Tidewell Crest Housekeeping</p>
    </div>
    <p class="tagline">more time for the moments that matter</p>
    <p class="web-address">tidewellcresthousekeeping.com</p>
  </div>
</section>

</body>
</html>
```